Summer Sale Graphics for Social Media

I want to create 11 social media graphics (new Instagram size 4:5 (1080 x 1350 pixels) focusing on our Summer Sale Graphics, using any of the pics attached. Use the attached pics, NO RANDOM STOCK PHOTOGRAPHY. For the color scheme of the graphics, they should all be complementary to the product colors in the photos.
You can add any of the photos attached but none are required. You can do some of the graphics in all text. I mainly need BOLD text that says one of the headlines (11 total) SEE ATTACHED WORD DOCUMENT for the headlines to use.

```html
<!DOCTYPE html>
<html lang="en">
<head>
<meta charset="utf-8">
<title>Summer Sale Social Graphics</title>
<link href="https://fonts.googleapis.com/css2?family=Anton&family=Oswald:wght@600;700&display=swap" rel="stylesheet">
<style>
:root{
  --ink:#111114;
  --red:#e8262c;
  --blue:#3b3fa3;
  --pink:#c95f9f;
  --green:#234a3d;
  --orange:#f47b20;
  --navy:#1d1f2b;
  --mist:#eceef6;
  --mint:#b9d9cf;
  --white:#ffffff;
}
*{margin:0;padding:0;box-sizing:border-box}
html,body{width:1200px;height:504px;overflow:hidden;background:#000}
.board{position:relative;width:1200px;height:504px;background:#000}
.tile{position:absolute;width:185px;height:231px;overflow:hidden;background:var(--white);font-family:'Anton',sans-serif;color:var(--ink);text-transform:uppercase}
.ribbon{position:absolute;left:-16px;top:12px;width:84px;height:9px;background:var(--orange);transform:rotate(-32deg);color:var(--white);font-family:'Oswald',sans-serif;font-weight:700;font-size:5px;line-height:9px;text-align:center;z-index:5}
.copy{position:absolute;left:0;right:0;text-align:center;line-height:.98;z-index:3}
.copy.left{text-align:left;left:16px}
.red{color:var(--red)}
.blue{color:var(--blue)}
.pinkt{color:var(--pink)}
.tag{background:var(--red);color:var(--white);padding:0 2px}
.bottles{position:absolute;display:flex;align-items:flex-end;gap:3px;z-index:2}
.bottle{display:block;border-radius:5px 5px 3px 3px;background:linear-gradient(90deg,#d9dbe0,#ffffff 45%,#cfd2d8)}
.bottle.s{width:26px;height:42px}
.bottle.m{width:34px;height:58px}
.bottle.l{width:42px;height:72px}
.bottle.xs{width:21px;height:36px}
.columns{position:absolute;left:16px;top:119px;width:153px;height:96px;display:flex;gap:2px}
.columns span{flex:1;border-radius:4px 4px 0 0}
.c1{background:var(--pink)}.c2{background:var(--red)}.c3{background:var(--green)}.c4{background:var(--blue)}
.model{position:absolute;border-radius:40% 40% 6px 6px;background:linear-gradient(180deg,#3a2a24 0%,#8a5a44 35%,#f2f2f2 60%,#e6e6ea 100%);z-index:1}
.halo{position:absolute;border-radius:50%;border:6px solid #dfe1ea;z-index:0}
.swoosh{position:absolute;right:-60px;top:-90px;width:170px;height:210px;border-radius:50%;background:var(--red);z-index:0}
.swoosh::after{content:"";position:absolute;left:-22px;top:20px;width:170px;height:220px;border-radius:50%;background:var(--mist)}
.base{position:absolute;left:0;right:0;bottom:0;z-index:0}
</style>
</head>
<body>
<div class="board">

<!-- Row 1 -->
<section class="tile" style="left:17px;top:19px;background:linear-gradient(180deg,#fff,#ececec)">
  <div class="ribbon">UPTO $50 OFF</div>
  <div class="base" style="height:50px;background:var(--navy);clip-path:polygon(0 40%,100% 0,100% 100%,0 100%)"></div>
  <div class="copy" style="top:22px;font-size:58px;letter-spacing:8px;padding-left:8px">SALE</div>
  <div class="copy" style="top:84px;font-size:20px"><span class="red">YOUR SUMMER BODY</span></div>
  <div class="copy" style="top:104px;font-size:30px">STARTS HERE</div>
  <div class="bottles" role="img" aria-label="Product photo: four supplement bottles" style="left:18px;top:143px"><span class="bottle s"></span><span class="bottle m"></span><span class="bottle m"></span><span class="bottle l"></span></div>
</section>

<section class="tile" style="left:214px;top:19px">
  <div class="ribbon">UPTO $50 OFF</div>
  <div class="copy" style="top:22px;font-size:21px">GET SNATCHED FOR</div>
  <div class="copy" style="top:44px;font-size:44px">SUMMER</div>
  <div class="copy" style="top:90px;font-size:13px">SUPPLEMENTS ON <span class="tag">SALE NOW!</span></div>
  <div class="columns"><span class="c1"></span><span class="c2"></span><span class="c3"></span><span class="c4"></span></div>
  <div class="bottles" role="img" aria-label="Product photo: four supplement bottles" style="left:18px;top:143px;gap:5px"><span class="bottle m"></span><span class="bottle m"></span><span class="bottle m"></span><span class="bottle m"></span></div>
</section>

<section class="tile" style="left:411px;top:19px">
  <div class="ribbon">UPTO $50 OFF</div>
  <div class="copy" style="top:22px;font-size:22px">FINAL COUNTDOWN</div>
  <div class="copy" style="top:44px;font-size:33px">TO SUMMER</div>
  <div class="copy red" style="top:78px;font-size:36px">SALE NOW!</div>
  <div class="columns"><span class="c1"></span><span class="c2"></span><span class="c3"></span><span class="c4"></span></div>
  <div class="bottles" role="img" aria-label="Product photo: four supplement bottles" style="left:18px;top:143px;gap:5px"><span class="bottle m"></span><span class="bottle m"></span><span class="bottle m"></span><span class="bottle m"></span></div>
</section>

<section class="tile" style="left:608px;top:19px">
  <div class="ribbon">UPTO $50 OFF</div>
  <div class="base" style="height:93px;background:var(--navy)"></div>
  <div class="copy" style="top:24px;font-size:29px">LIMITED-TIME</div>
  <div class="copy red" style="top:52px;font-size:29px">SUMMER SALE</div>
  <div class="bottles" role="img" aria-label="Product photo: four supplement bottles" style="left:26px;top:92px"><span class="bottle s"></span><span class="bottle m"></span><span class="bottle m"></span><span class="bottle l"></span></div>
  <div class="copy" style="top:172px;font-size:21px;color:var(--white)">SNATCH YOUR<br>SUPPLEMENTS NOW!</div>
</section>

<section class="tile" style="left:805px;top:19px">
  <div class="ribbon">UPTO $50 OFF</div>
  <div class="copy" style="top:30px;font-size:24px">YOUR <span class="blue">SUMMER</span><br><span class="blue">BODY</span> WON'T WAIT</div>
  <div class="copy red" style="top:76px;font-size:30px">SALE NOW!</div>
  <div class="columns"><span class="c1"></span><span class="c2"></span><span class="c3"></span><span class="c4"></span></div>
  <div class="bottles" role="img" aria-label="Product photo: four supplement bottles" style="left:18px;top:143px;gap:5px"><span class="bottle m"></span><span class="bottle m"></span><span class="bottle m"></span><span class="bottle m"></span></div>
</section>

<section class="tile" style="left:1003px;top:19px;background:var(--mist)">
  <div class="ribbon">UPTO $50 OFF</div>
  <div class="swoosh"></div>
  <div class="base" style="height:18px;background:var(--navy)"></div>
  <div class="copy left" style="top:32px;font-size:15px">SUMMER'S HERE.<br>AND WE'RE HAVING</div>
  <div class="copy left" style="top:68px;font-size:27px"><span class="red">THE BIGGEST<br>SALE</span> OF<br>THE YEAR</div>
  <div class="halo" style="left:124px;top:100px;width:60px;height:60px"></div>
  <div class="model" role="img" aria-label="Photo of smiling woman in white crop top holding a supplement bottle" style="left:128px;top:112px;width:54px;height:119px"></div>
  <div class="bottles" role="img" aria-label="Product photo: four supplement bottles" style="left:12px;top:185px;gap:6px"><span class="bottle xs"></span><span class="bottle xs"></span><span class="bottle xs"></span><span class="bottle xs"></span></div>
</section>

<!-- Row 2 -->
<section class="tile" style="left:17px;top:259px;background:linear-gradient(180deg,#fff,#ececec)">
  <div class="ribbon">UPTO $50 OFF</div>
  <div class="base" style="height:55px;background:var(--navy);clip-path:polygon(0 55%,100% 10%,100% 100%,0 100%)"></div>
  <div class="copy left" style="top:26px;font-size:24px;text-transform:none">Detox, Burn Fat,<br><span class="red">and Turn Heads</span><br>This Summer</div>
  <div class="copy left" style="top:104px;font-size:22px;left:16px"><span class="tag" style="padding:0 6px">SALE NOW!</span></div>
  <div class="bottles" role="img" aria-label="Product photo: four supplement bottles" style="left:18px;top:137px"><span class="bottle s"></span><span class="bottle m"></span><span class="bottle m"></span><span class="bottle l"></span></div>
</section>

<section class="tile" style="left:214px;top:259px;background:var(--mist)">
  <div class="ribbon">UPTO $50 OFF</div>
  <div class="swoosh"></div>
  <div class="base" style="height:20px;background:var(--navy)"></div>
  <div class="copy left" style="top:36px;font-size:14px">SUMMER'S HERE.<br>AND WE'RE HAVING</div>
  <div class="copy left" style="top:68px;font-size:26px"><span class="red">THE BIGGEST<br>SALE</span> OF<br>THE YEAR</div>
  <div class="halo" style="left:122px;top:98px;width:62px;height:62px"></div>
  <div class="model" role="img" aria-label="Photo of smiling woman in white crop top holding a supplement bottle" style="left:128px;top:108px;width:56px;height:123px"></div>
  <div class="bottles" role="img" aria-label="Product photo: four supplement bottles" style="left:12px;top:176px;gap:4px"><span class="bottle s"></span><span class="bottle s"></span><span class="bottle s"></span><span class="bottle s"></span></div>
</section>

<section class="tile" style="left:411px;top:259px;background:var(--mist)">
  <div class="ribbon">UPTO $50 OFF</div>
  <div class="swoosh"></div>
  <div class="base" style="height:20px;background:var(--navy)"></div>
  <div class="copy left" style="top:36px;font-size:23px">ONE SALE.<br>ONE BODY.<br><span class="red">ONE SUMMER<br>TO SLAY</span></div>
  <div class="halo" style="left:124px;top:104px;width:60px;height:60px"></div>
  <div class="model" role="img" aria-label="Photo of smiling woman in white crop top holding a supplement bottle" style="left:130px;top:114px;width:54px;height:117px"></div>
  <div class="bottles" role="img" aria-label="Product photo: four supplement bottles" style="left:12px;top:176px;gap:4px"><span class="bottle s"></span><span class="bottle s"></span><span class="bottle s"></span><span class="bottle s"></span></div>
</section>

<section class="tile" style="left:608px;top:259px;background:var(--mist)">
  <div class="ribbon">UPTO $50 OFF</div>
  <div class="swoosh"></div>
  <div class="base" style="height:30px;background:linear-gradient(180deg,#f4f4f4,#dcdcdc)"></div>
  <div class="copy left" style="top:24px;font-family:'Oswald',sans-serif;font-weight:700;font-size:25px;line-height:.98;text-transform:none;color:var(--blue)">Summer<br>isn't Waiting<br>Neither<br>Should You</div>
  <div class="copy left" style="top:138px;font-size:24px"><span class="red">SALE</span> NOW!</div>
  <div class="model" role="img" aria-label="Photo of smiling woman in white crop top holding a supplement bottle" style="left:140px;top:98px;width:45px;height:102px"></div>
  <div class="bottles" role="img" aria-label="Product photo: four supplement bottles and two small bottles" style="left:12px;top:172px;gap:4px"><span class="bottle s"></span><span class="bottle s"></span><span class="bottle s"></span><span class="bottle s"></span><span class="bottle" style="width:8px;height:14px"></span><span class="bottle" style="width:8px;height:14px"></span></div>
</section>

<section class="tile" style="left:805px;top:259px">
  <div class="ribbon">UPTO $50 OFF</div>
  <div class="base" style="height:30px;background:linear-gradient(180deg,#f4f4f4,#dcdcdc)"></div>
  <div class="copy" style="top:18px;font-size:24px;line-height:1.02">SLIM <span class="red">WAIST</span>.<br>FLAT <span class="blue">TUMMY</span>.<br>MORE <span class="blue">ENERGY</span>.</div>
  <div class="copy pinkt" style="top:97px;font-size:22px;padding-right:8px">LET'S GO!</div>
  <div class="copy left" style="top:138px;font-size:24px"><span class="red">SALE</span> NOW!</div>
  <div class="model" role="img" aria-label="Photo of smiling woman in white crop top holding a supplement bottle" style="left:140px;top:98px;width:45px;height:102px"></div>
  <div class="bottles" role="img" aria-label="Product photo: four supplement bottles and two small bottles" style="left:12px;top:172px;gap:4px"><span class="bottle s"></span><span class="bottle s"></span><span class="bottle s"></span><span class="bottle s"></span><span class="bottle" style="width:8px;height:14px"></span><span class="bottle" style="width:8px;height:14px"></span></div>
</section>

<section class="tile" style="left:1003px;top:259px;background:var(--green);color:var(--white)">
  <div class="ribbon">UPTO $50 OFF</div>
  <div class="base" style="height:75px;background:var(--mint)"></div>
  <div class="copy" style="top:16px;font-size:32px;letter-spacing:1px">HURRY</div>
  <div class="copy" style="top:46px;font-size:25px">OUR SUMMER<br>SLIM-DOWN</div>
  <div class="copy" style="top:96px"><span style="display:inline-block;background:var(--mint);color:var(--green);font-size:24px;padding:0 10px;clip-path:polygon(0 0,100% 0,94% 50%,100% 100%,0 100%,6% 50%)">SALE IS ON!</span></div>
  <div class="copy" style="top:123px;font-size:22px">DON'T MISS IT!</div>
  <div class="bottles" role="img" aria-label="Product photo: four supplement bottles" style="left:28px;top:146px"><span class="bottle s"></span><span class="bottle m"></span><span class="bottle m"></span><span class="bottle l"></span></div>
</section>

</div>
</body>
</html>
```